Australia-Wide Industry Leader Bookkeeping Business Website Design Required

We need a website designed for our 10 year old bookkeeping business, Barwick & Lund. Barwick & Lund has been servicing the local & interstate communities of Australia, providing first-class BAS & Bookkeeping services with a personal touch unmatched by anyone else in the county.

What began 10 years ago as a small business focusing on family, friends and the local community, it has since grown into a well respected business with 95% of their business based solely on word of mouth and personal referrals from around Australia.

We would like to see designs that incorporate our existing brand/logo. The colours to be used on the website should be colours that work well with our logo. The design should communicate maturity, trust and confidence with a Web 2.0 look and feel.

We have produced mockups of the entire website as well as assets used in the mockups. Please reference the attached files. The mockups are an example of all the design elements that we want on each page. Designers are encouraged to use the mockups as a guideline only and for designers to use their own creativity.
Updates

This message is for new graphic designers who are considering commencing work on this project. Thank you for expressing an interest in our project. We would like to inform you that this project is close to completion as we have a number designs under very serious consideration.

We are currently in a position where we are disinterested providing feedback to improve on new designs submitted. We will provide feedback to improve new designs only if the submitted designs are very close to what we want for our website, and will only require 1 or 2 revision rounds to refine before the project completion date we will not work with designers to refine their newly submitted designs.

We feel that it is important for all designers to know the above information as we feel that your time and effort may be better spent working on another project.

Thank you for your understanding.

A big thank you for all the designs submitted. We are now in the process of selecting a design. Please be patient during this process. Thank you.

Target Market(s)

Busy Business Owners

Industry/Entity Type

Small Business

Requirements
Must have
• We require a rectangular "slide show" type feature to serve as a "teaser" to arouse the emotions of our website visitors. Each slide asks a specific question. The questions are:

- Is your paperwork in a mess?
- Do you need to get organised for the end of financial year?
- Are you sick & tired of endless amounts of paperwork & BASs?
- Do you feel frustrated & annoyed because you know your books need to be done?
- Do you lack the time & patience to get your paperwork done?
- Do you wish you had more time to do the things you enjoy doing?
- Contact Barwick & Lund today and we will transform your chaos into order.

Underneath the slide show will be a button to "Call Barwick & Lund Now - 03 5550 1827".

```html
<!DOCTYPE html>
<html lang="en">
<head>
<meta charset="utf-8">
<title>Barwick &amp; Lund – BAS &amp; Bookkeeping</title>
<link rel="stylesheet" href="https://fonts.googleapis.com/css2?family=Mulish:wght@400;700&family=Arimo:wght@400;700&display=swap">
<style>
:root{
  --red:#a80000;
  --red-dark:#8a0000;
  --hero:#b00002;
  --grey-text:#6b6b6b;
  --grey-mid:#8c8c8c;
  --nav-top:#a8a8a8;
  --nav-bottom:#7a7a7a;
  --orange-top:#fcc63a;
  --orange-bottom:#f0a01c;
  --tick:#f29a1d;
  --page:#ffffff;
}
*{margin:0;padding:0;box-sizing:border-box}
html,body{width:1200px;height:900px;overflow:hidden}
body{position:relative;background:var(--page);font-family:'Arimo',Arial,sans-serif;color:var(--grey-text)}
.header-band{position:absolute;left:0;top:0;width:1200px;height:170px;background:linear-gradient(#ececec,#ffffff 60%,#f4f4f4)}
.brand{position:absolute;left:120px;top:31px;width:366px;height:71px;display:flex;align-items:center;gap:14px;padding-left:14px;border:1px solid #222;background:#fff}
.brand-square{width:34px;height:34px;background:var(--red)}
.brand-name{font-family:'Mulish',sans-serif;font-weight:700;font-size:38px;color:#1a1a1a;letter-spacing:-.5px}
.files-art{position:absolute;left:808px;top:38px;width:80px;height:84px;border-radius:4px;background:linear-gradient(#7fa6b8 0%,#6f8f9a 55%,#b7763a 56%,#8c5426 100%)}
.header-call{position:absolute;left:899px;top:66px;font-family:'Mulish',sans-serif}
.header-call .label{font-size:16px;font-weight:700;color:#8e8e8e}
.header-call .number{font-size:26px;font-weight:700;color:var(--red);margin-top:-2px;letter-spacing:.5px}
.main-nav{position:absolute;left:120px;top:125px;width:960px;height:45px;border-radius:5px 5px 0 0;background:linear-gradient(var(--nav-top),var(--nav-bottom));display:flex;align-items:center;padding-left:24px;gap:28px}
.main-nav a{font-family:'Mulish',sans-serif;font-weight:700;font-size:14px;color:#fff;text-decoration:none;letter-spacing:.3px}
.hero{position:absolute;left:0;top:170px;width:1200px;height:338px;background:var(--red-dark)}
.hero-stage{position:absolute;left:120px;top:0;width:960px;height:338px;background:radial-gradient(circle at 65% 40%,#c40a0a,var(--hero) 50%,#960000)}
.hero-art{position:absolute;left:120px;top:0;width:520px;height:338px;background:linear-gradient(90deg,rgba(110,95,85,.0),rgba(120,105,95,.55) 25%,rgba(230,225,215,.75) 65%,rgba(200,190,180,.0))}
.slide-arrow{position:absolute;top:157px;width:64px;height:64px}
.slide-arrow.prev{left:141px}
.slide-arrow.next{left:996px}
.slide-question{position:absolute;left:672px;top:64px;color:#fff;font-family:'Mulish',sans-serif;font-size:20px;line-height:30px}
.slide-question strong{font-size:28px;font-weight:700}
.call-button{position:absolute;left:662px;top:216px;width:313px;height:84px;border-radius:8px;background:linear-gradient(var(--orange-top),var(--orange-bottom));box-shadow:0 2px 4px rgba(0,0,0,.3);text-align:center;color:#fff;font-family:'Mulish',sans-serif;font-weight:700}
.call-button .label{font-size:24px;padding-top:10px}
.call-button .number{font-size:34px;line-height:34px;letter-spacing:1px}
.intro-strip{position:absolute;left:0;top:508px;width:1200px;height:65px;background:linear-gradient(#ffffff,#e9e9e9)}
.intro-icon{position:absolute;left:136px;top:526px}
.intro-text{position:absolute;left:170px;top:520px;width:900px;font-family:'Mulish',sans-serif;font-weight:700;font-size:15px;line-height:21px;color:#888}
.content{position:absolute;left:140px;top:592px;width:642px}
.content h2{font-family:'Mulish',sans-serif;font-weight:700;font-size:16px;color:var(--red);margin-left:3px}
.content p{font-size:12px;line-height:20px;color:var(--grey-text);margin-top:8px}
.content h3{font-family:'Mulish',sans-serif;font-weight:700;font-size:16px;color:var(--red);margin-top:12px}
.points{list-style:none;margin-top:10px}
.points li{display:flex;align-items:center;gap:8px;font-size:12px;height:24px;color:var(--grey-text)}
.coverage{position:absolute;left:808px;top:595px;width:273px;height:320px;border:1px solid #d8d8d8;background:#fff;box-shadow:0 0 3px rgba(0,0,0,.08)}
.coverage h4{position:absolute;left:16px;top:13px;font-family:'Mulish',sans-serif;font-weight:700;font-size:17px;color:var(--red)}
.coverage .rule{position:absolute;left:16px;top:37px;width:190px;border-top:2px dashed #c8c8c8}
.paperclip{position:absolute;left:1034px;top:580px}
.map-art{position:absolute;left:12px;top:48px;width:252px;height:200px;border-radius:40% 45% 35% 40%;background:radial-gradient(circle at 50% 45%,#e4e4e4,#cfcfcf)}
.coverage .stat{position:absolute;left:16px;top:248px;width:245px;font-size:12px;line-height:20px;font-weight:700;color:var(--grey-text)}
.coverage .stat b{font-size:24px;color:var(--red)}
</style>
</head>
<body>
<div class="header-band"></div>

<div class="brand"><span class="brand-square"></span><span class="brand-name">Barwick &amp; Lund</span></div>

<div class="files-art" role="img" aria-label="Illustration of ring binder files in a wooden tray"></div>
<div class="header-call"><div class="label">Call Us Now:</div><div class="number">03 5550 1827</div></div>

<nav class="main-nav">
  <a href="#">HOME</a><a href="#">ABOUT US</a><a href="#">SERVICES</a><a href="#">TESTIMONIALS</a><a href="#">ARTICLE</a><a href="#">ENDORSEMENTS</a><a href="#">LINKS</a><a href="#">CONTACT US</a>
</nav>

<section class="hero">
  <div class="hero-stage"></div>
  <div class="hero-art" role="img" aria-label="Illustration of a stressed business woman beside towering piles of paperwork and a filing cabinet"></div>
  <svg class="slide-arrow prev" viewBox="0 0 64 64"><circle cx="32" cy="32" r="30" fill="#8a2a2a" stroke="#d9a9a9" stroke-width="3"/><path d="M40 22H28V14L14 32l14 18v-8h12z" fill="#fff" transform="translate(4 0)"/></svg>
  <svg class="slide-arrow next" viewBox="0 0 64 64"><circle cx="32" cy="32" r="30" fill="#8a2a2a" stroke="#d9a9a9" stroke-width="3"/><path d="M24 22h12v-8l14 18-14 18v-8H24z" fill="#fff" transform="translate(-4 0)"/></svg>
  <div class="slide-question">Do you feel <strong>frustrated &amp; annoyed</strong><br>because you know your books need<br>to be done?</div>
  <div class="call-button"><div class="label">Call Us Now</div><div class="number">03 5550 1827</div></div>
</section>

<div class="intro-strip"></div>
<svg class="intro-icon" width="26" height="30" viewBox="0 0 26 30"><rect x="0" y="0" width="26" height="30" fill="#8a8a8a"/><path d="M6 4h6v14l-3-3-3 3z" fill="#fff"/></svg>
<p class="intro-text">For nearly 10 years Barwick &amp; Lund has been servicing the local &amp; interstate communities of Australia, providing first-class BAS &amp; Bookkeeping services with a personal touch unmatched by anyone else in the county.</p>

<main class="content">
  <h2>Welcome to Barwick &amp; Lund</h2>
  <p>Having worked for a Certified Accountants firm for numerous years, Helen Barwick &amp; Rachel Lund became concerned about the consistency of inaccurate books prepared by others in various organisations, As the quality of bookwork declined, the fees seemed to increase, Together they identified a need for a quality bookkeeping service that truly understood what being in business is all about and more importantly, how to correctly &amp; accurately process books according to the laws and requirements set by the Australian Taxation Office They wanted to give people a better alternative&nbsp; thus Barwick &amp; Lund was born What began as a small business focusing on family, friends and the local community, has since grown into a&nbsp; well respected business with 95% of their business based solely on word of mouth and personal referrals from around Australia.</p>
  <h3>What makes Barwick &amp; Lund different from other Bookkeepers</h3>
  <ul class="points">
    <li><svg width="18" height="14" viewBox="0 0 18 14"><path d="M1 7l5 5L17 2l-2-2-9 8-3-3z" fill="var(--tick)"/></svg>We guarantee the quality of our work</li>
    <li><svg width="18" height="14" viewBox="0 0 18 14"><path d="M1 7l5 5L17 2l-2-2-9 8-3-3z" fill="var(--tick)"/></svg>We have over 35 years of experience</li>
    <li><svg width="18" height="14" viewBox="0 0 18 14"><path d="M1 7l5 5L17 2l-2-2-9 8-3-3z" fill="var(--tick)"/></svg>We have owned &amp; operated businesses for 35 years</li>
    <li><svg width="18" height="14" viewBox="0 0 18 14"><path d="M1 7l5 5L17 2l-2-2-9 8-3-3z" fill="var(--tick)"/></svg>The Barwick &amp; Lund team are proud members of the industry</li>
  </ul>
</main>

<aside class="coverage">
  <h4>Servicing All of Australia</h4>
  <div class="rule"></div>
  <div class="map-art" role="img" aria-label="Map of Australia with client locations marked in each state"></div>
  <p class="stat"><b>95%</b> of our clients come from client &amp; accountant referrals we have clients all over victoria, Queensland, NSW &amp; Western Australia</p>
</aside>
<svg class="paperclip" width="46" height="70" viewBox="0 0 46 70"><path d="M10 62L36 16a8 8 0 0 0-14-8L4 42a5 5 0 0 0 9 5l16-28" fill="none" stroke="#9a9a9a" stroke-width="3" stroke-linecap="round"/></svg>
</body>
</html>
```